Norwick Staffing Partners, Inc. Corporate Profile

I need a new corporate profile. I have attached a photoshop sample file and then a PowerPoint of what I need and the order I need it in. I want to create the new profile from the Vellum Quarry design using the Norwick Presentation powerpoint. The pages should be in the Norwick Presentation Powerpoint. I am available for any questions. This should be 16 total pages and needs a very slick, bold cover page.

Industry/Entity Type

Financial Service

Font styles to use
Serif
Sans Serif

Requirements
Must have
• Bold, professional, colorful

```html
<!DOCTYPE html>
<html lang="en">
<head>
<meta charset="utf-8">
<title>Norwick Staffing Partners – Corporate Profile</title>
<link href="https://fonts.googleapis.com/css2?family=Merriweather:wght@400;700&family=Arimo:wght@400;700&display=swap" rel="stylesheet">
<style>
:root{
  --bg:#1c1c1c;
  --paper:#ffffff;
  --brown:#8a5a2e;
  --brown-dark:#5e3413;
  --tag:#6b4a2f;
  --ink:#222222;
  --muted:#555555;
  --blue:#2a5bd7;
  --slate:#3d4346;
  --night:#0d1030;
  --rule:#bdbdbd;
}
*{box-sizing:border-box;margin:0;padding:0}
html,body{width:1200px;height:800px;overflow:hidden}
body{background:var(--bg);position:relative;font-family:"Arimo",Arial,sans-serif;color:var(--ink)}
.page{position:absolute;top:214px;width:270px;height:372px;background:var(--paper);overflow:hidden;border-bottom:7px solid var(--brown-dark)}
.p1{left:30px}.p2{left:320px}.p3{left:610px}.p4{left:900px}
.abs{position:absolute}
.brand{display:flex;align-items:center;gap:5px;font-family:"Merriweather",Georgia,serif;font-size:8px;color:var(--brown)}
.brand .mark{width:9px;height:9px;background:var(--brown)}
.brand-small{font-size:5px;gap:3px}
.brand-small .mark{width:7px;height:7px}
/* cover */
.cover-head{left:14px;top:22px;height:34px;width:242px;display:flex;align-items:center}
.cover-head .divider{width:1px;height:30px;background:var(--rule);margin:0 10px}
.cover-head address{font-style:normal;font-size:4.5px;line-height:1.5;color:var(--muted)}
.cover-photo{left:0;top:70px;width:270px;height:130px;background:linear-gradient(180deg,#cfe3e0 0%,#6aa9a2 45%,#2f6c67 100%)}
.cover-panel{left:0;top:200px;width:270px;height:172px;background:linear-gradient(180deg,#4a5255,var(--slate))}
.thumbs{right:0;top:150px;width:54px;display:flex;flex-direction:column;gap:5px}
.thumbs span{display:block;height:42px;border:2px solid #fff;background:#d9dde0}
.thumbs span:nth-child(2){background:linear-gradient(135deg,#e04b5a,#5a7bd8)}
.thumbs span:nth-child(3){background:linear-gradient(135deg,#9fb8cf,#2f4e6e)}
.thumbs span:nth-child(4){background:#eef1f3}
/* who we are */
.who-title{left:18px;top:28px;font-size:15px;font-weight:700;color:var(--blue)}
.who-photo{left:0;top:48px;width:270px;height:120px;background:linear-gradient(180deg,#2a3fc4 0%,#1b2a7a 45%,var(--night) 60%,#ffcc33 75%,#3a7bd8 88%,#10123a 100%)}
.who-quote{left:14px;top:82px;background:rgba(60,50,40,.6);padding:4px 8px;font-family:"Merriweather",Georgia,serif;font-size:11px;line-height:1.45;color:#fff}
.block{left:12px;width:246px;display:flex;gap:8px}
.block .pic{flex:0 0 70px;height:44px}
.mission{top:220px}.mission .pic{background:linear-gradient(135deg,#3a2a18,#111)}
.vision{top:278px}.vision .pic{background:linear-gradient(135deg,#d9a62a,#6b4a12)}
.block h3{font-family:"Merriweather",Georgia,serif;font-size:8.5px;margin-bottom:3px}
.block p{font-size:4.6px;line-height:1.45;color:var(--muted)}
.dots{left:14px;width:242px;border-top:1px dotted var(--rule)}
/* what we do */
.logo-tr{right:12px;top:20px}
.wwd-band{left:0;top:70px;width:270px;height:150px;background:linear-gradient(180deg,#2b2b2b,#151515)}
.wwd-title{left:12px;top:56px;font-size:14px;font-weight:700;color:var(--ink)}
.tags{left:10px;top:82px;display:flex;flex-direction:column;gap:4px}
.tags li{list-style:none;background:var(--tag);color:#fff;font-family:"Merriweather",Georgia,serif;font-size:9.5px;padding:3px 8px;width:max-content}
.bullets{left:16px;top:232px;width:240px;font-size:4.6px;line-height:1.5;color:var(--ink)}
.bullets li{margin-left:6px}
.affil{left:12px;top:300px;width:100px}
.affil h4{font-size:7px;color:#b4461c;margin-bottom:8px}
.badges{display:flex;gap:6px;align-items:center}
.badges span{width:16px;height:16px;background:#2e5aa8}
.badges span:nth-child(2){border-radius:50%;background:#1e2a44}
.badges span:nth-child(4){width:20px;height:11px;background:#c22}
.facts{left:150px;top:292px;border-left:1px dotted var(--rule);padding-left:8px;font-family:"Merriweather",Georgia,serif}
.facts dt{font-size:7.5px;font-weight:700}
.facts dd{font-size:4.8px;margin-bottom:4px;color:var(--muted)}
/* pieces */
.banner{left:0;top:118px;background:var(--brown);padding:5px 10px 4px 16px}
.banner h2{font-size:13px;font-weight:700;color:#2b1a0c}
.banner-sub{left:16px;top:143px;background:var(--brown-dark);color:#fff;font-size:6px;padding:2px 8px}
.cols{left:14px;width:246px;display:grid;grid-template-columns:repeat(3,1fr);gap:10px}
.cols.top{top:180px}.cols.bottom{top:290px}
.cols h5{font-family:"Merriweather",Georgia,serif;font-size:5px;font-weight:400;margin-bottom:2px}
.cols p{font-size:4.2px;line-height:1.45;color:var(--muted)}
.c-blue{color:#2f7fd8}.c-green{color:#6bbf2a}.c-red{color:#c0392b}.c-teal{color:#2ea59b}.c-orange{color:#e67e22}.c-purple{color:#7a1f4b}
.pieces{left:12px;top:245px;display:flex}
.pieces span{width:41px;height:36px;display:flex;align-items:center;justify-content:center;color:#fff;font-weight:700;font-size:13px;border-radius:3px}
</style>
</head>
<body>

<section class="page p1">
  <header class="abs cover-head">
    <div class="brand"><span class="mark"></span>Norwick Staffing Partners</div>
    <span class="divider"></span>
    <address>418 Harlow Ridge Dr. Cedar Bend, MO 63099<br>Phone : (800) 555-0142</address>
  </header>
  <div class="abs cover-photo" role="img" aria-label="River view of a city skyline with a large arch, teal toned"></div>
  <div class="abs cover-panel" role="img" aria-label="Dark slate panel with faint business analytics doodles"></div>
  <div class="abs thumbs" role="img" aria-label="Column of business thumbnails: compliance, charts, data, research">
    <span></span><span></span><span></span><span></span><span></span>
  </div>
</section>

<section class="page p2">
  <h2 class="abs who-title">Who We Are?</h2>
  <div class="abs who-photo" role="img" aria-label="City skyline and arch at night reflected in the river"></div>
  <p class="abs who-quote">Norwick (Nor-wick):<br>A quantitative<br>change.</p>
  <div class="abs dots" style="top:212px"></div>
  <div class="abs block mission">
    <div class="pic" role="img" aria-label="Dark board with the word mission"></div>
    <div><h3>Our Mission</h3><p>“At Norwick Staffing Partners, Inc. our mission is to provide professional and compliant receivables management built on integrity, transparency and accountability, delivering superior results through skilled people and analytics.”</p></div>
  </div>
  <div class="abs block vision">
    <div class="pic" role="img" aria-label="Photo of a dart hitting a gold target"></div>
    <div><h3>Corporate Vision</h3><p>“Norwick Staffing Partners remains committed to controlled growth achieved by consistently providing clients superior performance and customer service while keeping a vigilant eye on compliance.”</p></div>
  </div>
  <div class="abs dots" style="top:340px"></div>
</section>

<section class="page p3">
  <div class="abs logo-tr brand brand-small"><span class="mark"></span>Norwick Staffing Partners</div>
  <div class="abs wwd-band" role="img" aria-label="Dark city skyline silhouette"></div>
  <h2 class="abs wwd-title">What We Do</h2>
  <ul class="abs tags">
    <li>PRE CHARGE/ EARLY OUT</li>
    <li>PRE &amp; POST LEGAL</li>
    <li>POST CHARGE OFF</li>
    <li>SKIP TRACING</li>
    <li>CUSTOMER CARE</li>
  </ul>
  <ul class="abs bullets">
    <li>Nationwide provider of collection and receivable management programs.</li>
    <li>Licensed, insured, bonded and registered to collect nationwide.</li>
    <li>Built an infrastructure to meet demanding challenges of the industry.</li>
    <li>Employs a highly experienced and motivated workforce using modern technology.</li>
    <li>Full call center capabilities covering the entire cycle of an account.</li>
  </ul>
  <div class="abs dots" style="top:288px"></div>
  <div class="abs affil">
    <h4>Affiliations</h4>
    <div class="badges"><span></span><span></span><span></span><span></span></div>
  </div>
  <dl class="abs facts">
    <dt>Date Incorporated</dt><dd>07/02/2009</dd>
    <dt>Years in Business</dt><dd>07</dd>
    <dt>Company Location</dt><dd>418 Harlow Ridge Dr.</dd>
  </dl>
  <div class="abs dots" style="top:350px"></div>
</section>

<section class="page p4">
  <div class="abs logo-tr brand brand-small"><span class="mark"></span>Norwick Staffing Partners</div>
  <div class="abs banner"><h2>Staying Ahead of the Curve</h2></div>
  <div class="abs banner-sub">The P.I.E.C.E.S. to Our Success</div>
  <div class="abs cols top">
    <div><h5 class="c-blue">Professional Approach</h5><p>All employees are required to act professional and respectful at all times.</p></div>
    <div><h5 class="c-green">Employee Development</h5><p>Our employees are the foundation for which our success hinges, so we develop them.</p></div>
    <div><h5 class="c-red">Extraordinary Service</h5><p>Our service to partners and consumers must always exceed their expectations.</p></div>
  </div>
  <div class="abs pieces">
    <span style="background:#2f7fd8">P</span><span style="background:#2ea59b">I</span><span style="background:#6bbf2a">E</span><span style="background:#f39c12">C</span><span style="background:#e74c3c">E</span><span style="background:#7a1f4b">S</span>
  </div>
  <div class="abs cols bottom">
    <div><h5 class="c-teal">Innovative Technology</h5><p>We strive to stay up to date with the latest technology that benefits our partners.</p></div>
    <div><h5 class="c-orange">Create Opportunities</h5><p>We look to create opportunities in each aspect of what we do.</p></div>
    <div><h5 class="c-purple">Strong Performance</h5><p>All of our pieces are important, but a strong performance keeps us at the top.</p></div>
  </div>
</section>

</body>
</html>
```